Web Design Home Page

KRVL Athletics.com – Homepage Vision
KRVL is a community based youth sports program currently running basketball and soccer programs. We run recreational leagues, competitive club programs and run many camps, clinics and development programs in both sports.
My vision on the KRVL Home page was to design a clean page that will guide viewers quickly to the sport of interest.
At the top I was thinking of a KRVL Logo Bar. I want something that we can also customize for each of the sports to use in the future. So, 5 different logo bars.
1 – KRVL Athletics Logo Bar – Goes on the KRVLAthletics.com home page, which give general information about the club as a whole and leads folks to the sport they want to go.
2 – KRVL Basketball – Recreational. Same look as the homepage logo bar but only contains info regarding to recreational basketball.
3 – KRVL Basketball – Competitive. Same as above but only competitive basketball.
4 – KRVL Soccer – Recreational. Same as above but only recreational soccer.
5 – KRVL Soccer – Competitive. Same as above but only competitive soccer.
Maybe the logo bar on the home page can also be the main logo bar and also rotate the other 4 underneath the main logo bar. Logo are old, may need to be updated at some point.
The middle section, I was thinking of 4 boxes that when clicked on will take you to the appropriate website. The designs I used are just to show something. I took the picture off the web and they may be copyrighted so would probably need some type of original designs.
Recreational Basketball Website - http://krvlathletics-example.com/basketball/index.html
Competitive Basketball Website - http://www.krvlherons-example.com/
Recreational Soccer Website - http://krvlathletics-example.com/soccer/index.html
Competitive Soccer Website - http://www.ridgepremiersoccer-example.com/
Recreational basketball uses Granite Mesa Basketball (we own the trade name) or KRVL Basketball.
The competitive basketball club is known as KRVL Herons.
Recreational soccer goes by Granite Mesa Soccer or Granite Mesa Soccer Club.
Competitive soccer goes by Ridge Premier Soccer or Granite Mesa Soccer Club.
Then on the bottom of the page I was thinking of a menus bar that contains information general to the club (both basketball and soccer). When you click on any a pop up box will pop up with the information for each listed below.
About Us
Granite Mesa Athletic Club provides recreational leagues for both Basketball and Soccer with the focus placed on providing our youth with the rewarding opportunity of participating in youth sports. Our direction is to promote the recreational value of youth sports while emphasizing fun and respect for the sport.
Granite Mesa Athletic Club (KRVL) is based in the North Phoenix area with most of our players residing in the Willow Bend School District.
Our Mission
Our mission at Granite Mesa Athletic Club is to promote and develop excellence in youth sports based on skill, sportsmanship, values, and player character. Our programs aim to provide an environment for natural player development that prepares them for life experiences, both on and off the field.
We focus on a uniform sports philosophy throughout the club that emphasizes growth through positive reinforcement resulting in players achieving his/her fullest potential. We do not look for the next victory to measure our success, but in the total learning experience for each player, realizing that the team is much stronger than an individual.
Contact Info
Granite Mesa Athletic Club
P.O. Box 7068
Willow Bend, AZ 85990
Club Phone – 480-555-0173
Club Website – KRVLAthletics.com
Club Email – info@krvlathletics-example.com
Basketball Email – KRVLBB@mail-example.com
Soccer Email – KRVLSoccer@mail-example.com
Our Mission
The mission of KRVL shall be to promote good citizenship and health through community athletic activities for children and for educational purposes. Club focus is on player development, with emphasis on teamwork and sportsmanship with high standards for both parents and players. Respect, commitment and accountability are qualities we ask all our members to endorse both on and off the field.

```html
<!DOCTYPE html>
<html lang="en">
<head>
<meta charset="utf-8">
<title>Granite Mesa Athletic Club</title>
<link href="https://fonts.googleapis.com/css2?family=Oswald:wght@500&family=Signika:wght@400;600&family=Lato:wght@300;400&display=swap" rel="stylesheet">
<style>
:root{
  --navy:#0d2a6e;
  --nav-top:#2a5bb0;
  --nav-bottom:#0b2f7a;
  --ink:#1c3566;
  --body:#3a4a66;
  --soft:#4f6b94;
  --sky:#eef3fa;
  --orange:#f7941d;
  --orange-dark:#e9780a;
  --white:#ffffff;
  --line:#dbe3ee;
}
*{box-sizing:border-box;margin:0;padding:0}
html,body{width:969px;height:1200px;overflow:hidden;background:var(--white)}
body{position:relative;font-family:'Lato',sans-serif;color:var(--body)}
.abs{position:absolute}

.top-band{left:0;top:0;width:969px;height:559px;background:linear-gradient(#ffffff 0%,#f5f8fc 40%,var(--sky) 100%);border-top:2px solid #e3e6ec}

.club-title{left:0;width:969px;top:10px;text-align:center;font-family:'Signika',sans-serif;font-weight:600;font-size:19px;line-height:24px;color:var(--ink)}
.program-note{width:260px;text-align:center;font-family:'Signika',sans-serif;font-weight:600;font-size:12.5px;line-height:17px;color:var(--ink);top:20px}
.program-note.left{left:53px}
.program-note.right{left:617px}
.program-name{width:170px;text-align:center;font-family:'Signika',sans-serif;font-weight:600;font-size:12px;line-height:15px;color:#111;top:82px}
.program-name.left{left:98px}
.program-name.right{left:662px}

.main-nav{left:49px;top:140px;width:871px;height:47px;background:linear-gradient(var(--nav-top),var(--nav-bottom));border-radius:3px 3px 0 0}
.crest-bump{left:392px;top:40px;width:140px;height:140px;border-radius:50%;background:var(--white);border:3px solid var(--nav-top)}
.crest-name{left:392px;top:93px;width:140px;text-align:center;font-family:'Signika',sans-serif;font-weight:600;font-size:28px;line-height:34px;color:var(--navy)}
.nav-item{top:140px;height:47px;line-height:47px;font-family:'Oswald',sans-serif;font-weight:500;font-size:17px;color:var(--white);text-transform:uppercase;text-align:center;white-space:nowrap;transform:translateX(-50%)}
.nav-divider{top:140px;width:1px;height:47px;background:rgba(255,255,255,.22)}

.slider{left:49px;top:187px;width:871px;height:351px;background:var(--white);box-shadow:0 2px 4px rgba(0,0,0,.12)}
.slide-photo{left:55px;top:190px;width:859px;height:341px;background:radial-gradient(ellipse at 50% 60%,#2a2f45 0%,#4b3a32 30%,#cf9660 55%,#e3b482 100%)}
.slide-arrow{top:331px}
.slide-dots{left:455px;top:512px}

.mission-title{left:55px;top:592px;font-family:'Signika',sans-serif;font-weight:600;font-size:20px;color:var(--navy)}
.mission-text{left:55px;top:624px;width:560px;font-size:11px;line-height:18.7px;font-weight:400;color:var(--body)}
.mission-extra{left:55px;top:709px;width:560px;font-size:11px;line-height:18.7px;color:var(--soft)}

.mail-box{left:649px;top:579px;width:272px;height:166px;border:1px solid var(--line);border-radius:4px;background:linear-gradient(#ffffff,#f3f6fa)}
.mail-title{left:668px;top:595px;font-family:'Signika',sans-serif;font-weight:600;font-size:18px;color:var(--navy)}
.mail-text{left:668px;top:623px;width:245px;font-size:10px;line-height:17px;color:var(--ink)}
.mail-input{left:668px;top:664px;width:226px;height:26px;border:1px solid #cfd7e2;border-radius:4px;background:var(--white)}
.mail-button{left:811px;top:701px;width:84px;height:27px;border-radius:4px;background:linear-gradient(#fbab3a,var(--orange-dark));color:var(--white);font-family:'Signika',sans-serif;font-weight:600;font-size:13px;line-height:27px;text-align:center}

.sport-card{top:806px;width:209px;height:200px;background:linear-gradient(#ffffff,#e6edf6);box-shadow:0 8px 10px -6px rgba(40,70,120,.25)}
.sport-photo{position:absolute;left:0;top:0;width:209px;height:135px;clip-path:polygon(0 0,100% 0,100% 100%,0 88%)}
.sport-photo.ball{background:linear-gradient(#1c1c1c 0%,#b55a20 45%,#c27a3e 100%)}
.sport-photo.field{background:linear-gradient(#c9dcec 0%,#a8c6e0 40%,#5aa83a 62%,#3f8f28 100%)}
.sport-photo.hoop{background:linear-gradient(#0c2456 0%,#1f3f7a 55%,#d8742a 80%,#2a3f74 100%)}
.sport-photo.goal{background:linear-gradient(#8e8e96 0%,#d8d8dc 30%,#58b43a 55%,#2f8c22 100%)}
.sport-level{position:absolute;left:16px;top:149px;font-family:'Signika',sans-serif;font-size:16px;color:var(--navy)}
.sport-name{position:absolute;left:16px;top:166px;font-family:'Signika',sans-serif;font-weight:600;font-size:25px;color:var(--navy)}

.footer{left:0;top:1069px;width:969px;height:131px;background:linear-gradient(#2e5fb2 0%,#1f4a99 45%,#0f2f78 100%);border-top:6px solid #0a1f74}
.footer-links{left:55px;top:1105px;font-family:'Signika',sans-serif;font-weight:400;font-size:11.5px;color:var(--white);white-space:nowrap}
.footer-links span{color:rgba(255,255,255,.7);margin:0 6px}
.footer-copy{left:55px;top:1135px;font-size:10.5px;color:rgba(255,255,255,.8)}
.social{top:1100px;width:24px;height:24px;border-radius:50%;background:var(--white);box-shadow:0 1px 2px rgba(0,0,0,.3)}
</style>
</head>
<body>
<div class="abs top-band"></div>

<header>
  <div class="abs club-title">Granite Mesa Athletic Club</div>
  <div class="abs program-note left">Youth Basketball – Grades<br>K-12 Recreational and Competitive</div>
  <div class="abs program-name left">Granite Mesa<br>Basketball</div>
  <div class="abs program-note right">Youth Soccer Ages 3-18<br>Recreational and Competitive</div>
  <div class="abs program-name right">Granite Mesa<br>Soccer Club</div>

  <nav>
    <div class="abs main-nav"></div>
    <div class="abs crest-bump"></div>
    <div class="abs crest-name">KRVL</div>
    <div class="abs nav-item" style="left:153px">Home</div>
    <div class="abs nav-divider" style="left:190px"></div>
    <div class="abs nav-item" style="left:237px">About Us</div>
    <div class="abs nav-divider" style="left:285px"></div>
    <div class="abs nav-item" style="left:339px">Contact Us</div>
    <div class="abs nav-item" style="left:608px">Join KRVL Email List</div>
    <div class="abs nav-divider" style="left:686px"></div>
    <div class="abs nav-item" style="left:740px">Our Vision</div>
    <div class="abs nav-divider" style="left:790px"></div>
    <div class="abs nav-item" style="left:846px">Our Office</div>
  </nav>
</header>

<section>
  <div class="abs slider"></div>
  <div class="abs slide-photo" role="img" aria-label="Basketball player dunking at the rim on an indoor court, photographed from above"></div>
  <svg class="abs slide-arrow" style="left:68px" width="22" height="42" viewBox="0 0 22 42"><path d="M20 1 L2 21 L20 41" fill="none" stroke="#1c3a7a" stroke-width="1.6"/></svg>
  <svg class="abs slide-arrow" style="left:868px" width="22" height="42" viewBox="0 0 22 42"><path d="M2 1 L20 21 L2 41" fill="none" stroke="#1c3a7a" stroke-width="1.6"/></svg>
  <svg class="abs slide-dots" width="30" height="12" viewBox="0 0 30 12"><circle cx="6" cy="6" r="5" fill="#1f4fa0"/><circle cx="21" cy="6" r="5" fill="#8fa8cf"/></svg>
</section>

<main>
  <h2 class="abs mission-title">Our Mission</h2>
  <p class="abs mission-text">The mission of KRVL shall be to promote good citizenship and health through community athletic activities for children and for educational purposes. Club focus is on player development, with emphasis on teamwork and sportsmanship with high standards for both parents and players. Respect, commitment and accountability are qualities we ask all our members to endorse both on and off the field.</p>
  <p class="abs mission-extra">Nunc tempus felis vitae urna. Vivamus porttitor, g, purus nisi eleifend libero, a tempus libero lectus feugiat felis. Morbi diam mauris, viverra in, gravida eu, mattis in, ante. Morbi eget arcu.</p>

  <aside>
    <div class="abs mail-box"></div>
    <h3 class="abs mail-title">Join the KRVL Mail List</h3>
    <p class="abs mail-text">Join the email list to receive an occasional email from Granite Mesa Athletic Club</p>
    <div class="abs mail-input"></div>
    <div class="abs mail-button">Subscribe</div>
  </aside>

  <div class="abs sport-card" style="left:49px">
    <div class="sport-photo ball" role="img" aria-label="Basketball resting on a wooden court floor"></div>
    <div class="sport-level">Recreational</div>
    <div class="sport-name">Basketball</div>
  </div>
  <div class="abs sport-card" style="left:270px">
    <div class="sport-photo field" role="img" aria-label="Player kicking a soccer ball on grass"></div>
    <div class="sport-level">Recreational</div>
    <div class="sport-name">Soccer</div>
  </div>
  <div class="abs sport-card" style="left:490px">
    <div class="sport-photo hoop" role="img" aria-label="Basketball dropping through the hoop"></div>
    <div class="sport-level">Competitive</div>
    <div class="sport-name">Basketball</div>
  </div>
  <div class="abs sport-card" style="left:712px">
    <div class="sport-photo goal" role="img" aria-label="Soccer ball on the grass in front of a goal net"></div>
    <div class="sport-level">Competitive</div>
    <div class="sport-name">Soccer</div>
  </div>
</main>

<footer>
  <div class="abs footer"></div>
  <div class="abs footer-links">Home<span>/</span>About Us<span>/</span>Contact Us<span>/</span>Join KRVL Email List<span>/</span>Our Vision<span>/</span>Our Office</div>
  <div class="abs footer-copy">© 2012 Company Name.&nbsp; All right reserved. Term of Use</div>
  <div class="abs social" style="left:823px"></div>
  <div class="abs social" style="left:851px"></div>
  <div class="abs social" style="left:880px"></div>
</footer>
</body>
</html>
```